Frostwyn.co - Polar Expeditions Specialists

We need a modern, visually striking business card for Frostwyn.co, a company specialized in selling expedition cruises to the most remote regions on Earth, with a focus on the Arctic and Antarctica. The design should instantly communicate that the cardholder is an expert in polar travel. Use clean, premium aesthetics with cool tones like icy blue and white, possibly incorporating polar imagery (ice, glaciers, penguins, etc.)

Attached the logo

Contact Information for Business Card

Feels high-end and trustworthy.. Visually memorable — encourages people to keep it

Colors
0054AA
0677BA
7BADD7
CADEEF
E8F1F8

Requirements
Must have
• ice, glaciers, penguins, montains
Nice to have
• modern, transparente,

```html
<!DOCTYPE html>
<html lang="en">
<head>
<meta charset="UTF-8">
<title>Frostwyn.co – Business Card</title>
<link href="https://fonts.googleapis.com/css2?family=Poppins:wght@400;500;600;700&display=swap" rel="stylesheet">
<style>
  :root {
    --stage: #1c1d21;
    --night: #11122a;
    --paper: #ffffff;
    --ice-blue: #3474b4;
    --deep-blue: #0054aa;
    --sky-blue: #7badd7;
    --frost: #cadeef;
    --ink: #1a1a1a;
  }
  * { margin: 0; padding: 0; box-sizing: border-box; }
  html, body {
    width: 1200px; height: 900px; overflow: hidden;
    background: var(--stage);
    font-family: "Poppins", sans-serif;
  }
  .card {
    position: absolute;
    width: 640px; height: 366px;
    border-radius: 22px;
    overflow: hidden;
  }
  /* Back side */
  .card--back {
    left: 480px; top: 62px;
    background: var(--night);
    color: var(--paper);
    display: flex; flex-direction: column; align-items: center; justify-content: center;
  }
  .brand-dot {
    width: 70px; height: 70px; border-radius: 50%;
    background: var(--paper);
    margin-bottom: 22px;
  }
  .card--back .wordmark {
    font-size: 64px; font-weight: 700; letter-spacing: 1px; line-height: 1;
  }
  .card--back .tagline {
    font-size: 19px; font-weight: 500; margin-top: 10px; letter-spacing: .3px;
  }
  /* Front side */
  .card--front {
    left: 80px; top: 458px;
    background: var(--paper);
    color: var(--ink);
  }
  .front-brand {
    position: absolute; left: 40px; top: 32px;
    display: flex; align-items: center; gap: 18px;
    color: var(--ice-blue);
  }
  .front-brand .brand-dot { width: 64px; height: 64px; margin: 0; background: var(--ice-blue); }
  .front-brand .wordmark { font-size: 46px; font-weight: 700; line-height: 1; }
  .front-brand .tagline { font-size: 14px; font-weight: 600; margin-top: 4px; }
  .holder {
    position: absolute; left: 0; top: 140px;
    padding-left: 40px;
    border-left: 9px solid var(--ice-blue);
  }
  .holder__name { font-size: 27px; font-weight: 700; color: var(--ice-blue); line-height: 1.15; }
  .holder__role { font-size: 15px; font-weight: 400; }
  .address {
    position: absolute; left: 40px; top: 218px;
    font-size: 15px; line-height: 1.35; font-style: normal;
  }
  .contacts {
    position: absolute; left: 40px; top: 276px;
    list-style: none; font-size: 15px; line-height: 1.45;
  }
  .contacts li { display: flex; align-items: center; gap: 8px; }
  .contacts svg { width: 13px; height: 13px; fill: var(--ice-blue); flex: none; }
  .polar-artwork {
    position: absolute; left: 420px; top: 160px;
    width: 200px; height: 206px;
    border-radius: 100px 100px 0 0;
    background: linear-gradient(180deg, var(--sky-blue) 0%, var(--ice-blue) 45%, var(--deep-blue) 100%);
  }
</style>
</head>
<body>
  <section class="card card--back">
    <div class="brand-dot"></div>
    <div class="wordmark">Frostwyn.co</div>
    <div class="tagline">Polar Expeditions Specialists</div>
  </section>

  <section class="card card--front">
    <div class="front-brand">
      <div class="brand-dot"></div>
      <div>
        <div class="wordmark">Frostwyn.co</div>
        <div class="tagline">Polar Expeditions Specialists</div>
      </div>
    </div>

    <div class="holder">
      <div class="holder__name">Marlo Quenby</div>
      <div class="holder__role">CEO &amp; Founder</div>
    </div>

    <address class="address">
      42 Harbor Point Lane,<br>Camden, ME 04843 USA
    </address>

    <ul class="contacts">
      <li>
        <svg viewBox="0 0 16 16"><path d="M3.6 1.2l2.3 2.3-1.3 2a9 9 0 0 0 5.9 5.9l2-1.3 2.3 2.3-1.6 2.1C7.6 14.3 1.7 8.4 1.5 2.8z"/></svg>
        +1.555.014.278
      </li>
      <li>
        <svg viewBox="0 0 16 16"><path d="M1 3h14v1.2L8 9 1 4.2zM1 5.8l7 4.7 7-4.7V13H1z"/></svg>
        hello@frostwyn.co
      </li>
      <li>
        <svg viewBox="0 0 16 16"><circle cx="8" cy="8" r="7"/></svg>
        www.frostwyn.co
      </li>
    </ul>

    <div class="polar-artwork" role="img" aria-label="Large blue silhouette illustration of a polar bear standing with two penguins, with small sparkling stars above, rising from the bottom edge of the card"></div>
  </section>
</body>
</html>
```